Crypto Exchange Comparison Platform

Let’s design a page that lets users compare hundreds of cryptocurrency exchanges. It will help users compare more info than anywhere else so you can find the best crypto exchange for your needs. The goal is to transform complex data into a clean, visually engaging experience.

Key Features to Design:
- Interactive comparison table with ~ 30 columns
- Filters and dropdown menus for easier usability
- Summary boxes for quick-view statistics
- Visual charts and graphs for key metrics
- Web, mobile, and tablet responsive design

Design Goals:
- Clean, modern aesthetic that makes complex data easily digestible
- Interactive elements (eg. Bar and Spider charts) for user engagement
- "Screenshot-friendly" sections for social media and sharing
- Data visualization focus (charts, graphs, metrics)
- Extremely easy to use on mobile
- Designs that use the color green
- A brand that communicates research and trusted information

Deliverables:
- High-fidelity mockup for desktop, tablet, and mobile versions
- Interactive prototype (Figma preferred)
- Style guide (typography, colors, components)

Note: The goal is to create an intuitive, visually engaging tool that helps users compare cryptocurrency exchanges efficiently while maintaining a clean, professional appearance that works well for social media sharing and content creation.
Updates

Low design quality

Industry/Entity Type

FinTech, Crypto, Finance

Number of Pages Required

1 page

Font styles to use
Other font styles liked:
• Inter or something good for a finance/data related website site

Colors
00AB8E
00BBA5
67D7C9
C6EFE9
E9F9F6

Requirements
Must have
• Please refer to the sketch I uploaded

```html
<!DOCTYPE html>
<html lang="en">
<head>
<meta charset="utf-8">
<title>Compare – Crypto Exchange Comparison</title>
<link href="https://fonts.googleapis.com/css2?family=Inter:wght@400;500;600;700&family=Space+Grotesk:wght@500;600&display=swap" rel="stylesheet">
<style>
:root{
  --board:#0c3b31;--brand:#00AB8E;--brand2:#00BBA5;--brand3:#67D7C9;--brand4:#C6EFE9;--brand5:#E9F9F6;
  --red:#e5484d;--blue:#1652f0;--gold:#e8b100;--violet:#5741d9;--green:#19a64a;--orange:#f2a900;
}
*{box-sizing:border-box;margin:0;padding:0}
html,body{width:762px;height:1200px;overflow:hidden}
body{background:var(--board);font-family:Inter,Arial,sans-serif;position:relative}
.page{
  --bg:#fff;--ink:#121212;--muted:#6f6f6f;--soft:#f4f5f5;--line:#ececec;--card:#f7f7f7;--hi:#f5f5f7;
  --chip:#fff;--chipline:#e2e2e2;--hero:linear-gradient(180deg,#dff6f1 0%,#fff 55%);
  --foot:linear-gradient(180deg,#0f1e24,#0b1417);
  position:absolute;top:33.5px;width:662px;height:2288px;transform:scale(.498);transform-origin:0 0;
  background:var(--bg);color:var(--ink);overflow:hidden
}
.page.light{left:37.5px}
.page.dark{left:403.5px;--bg:#131313;--ink:#f2f2f2;--muted:#9a9a9a;--soft:#151515;--line:#262626;--card:#1c1c1c;--hi:#20222a;--chip:#1f1f1f;--chipline:#2e2e2e;--hero:linear-gradient(180deg,#161918 0%,#131313 60%);--foot:linear-gradient(180deg,#131313,#0f1a17)}
.abs{position:absolute}
.accent{color:var(--brand)}
/* nav */
.nav{top:0;left:0;right:0;height:44px;display:flex;align-items:center;padding:0 55px;background:var(--bg);border-bottom:1px solid var(--line)}
.brand{display:flex;align-items:center;gap:5px;font-weight:700;font-size:11px}
.brand-dot{width:26px;height:26px;border-radius:50%;background:var(--brand)}
.nav-links{display:flex;gap:14px;margin-left:37px;font-size:6.5px}
.mode{margin-left:37px;display:flex;background:var(--soft);border-radius:3px;font-size:7.5px;letter-spacing:.5px}
.mode span{padding:5px 9px}
.mode .on{background:#1a1a1a;color:#fff;border-radius:3px}
.dark .mode{background:transparent}.dark .mode .on{background:#262626}
.btn{background:var(--brand);color:#fff;font-weight:600;border-radius:3px;display:inline-flex;align-items:center;justify-content:center}
.nav .btn{margin-left:auto;font-size:6.5px;height:20px;width:71px}
/* hero */
.hero{top:44px;left:0;right:0;height:246px;background:var(--hero);text-align:center}
.hero .kicker{margin-top:57px;font-size:9.5px}
.hero h1{font-size:24px;font-weight:600;margin-top:8px;letter-spacing:-.2px}
.hero p{font-size:8px;line-height:13.5px;margin:12px auto 0;width:290px;color:var(--muted)}
.hero .btn{margin-top:19px;width:87px;height:24px;font-size:7px}
/* stats band */
.band{top:290px;left:0;right:0;height:62px;background:var(--soft);border-bottom:1px solid var(--line)}
.stat{position:absolute;top:17px}
.stat small{display:block;font-size:5px;font-weight:600;letter-spacing:.3px}
.stat b{display:block;font-family:"Space Grotesk",Inter,sans-serif;font-weight:600;font-size:10.5px;letter-spacing:1px;margin:2px 0 1px}
.ghost{position:absolute;border:1px solid var(--brand);border-radius:4px;font-size:6.5px;font-weight:500;display:flex;align-items:center;justify-content:center}
/* sections */
.eyebrow{font-size:7px}
.h2{font-size:18px;font-weight:500}
.center{left:0;right:0;text-align:center}
.center .h2{font-size:17.5px;margin-top:6px}
.cards{top:454px;left:55px;width:551px;display:grid;grid-template-columns:repeat(4,1fr);gap:6px}
.xcard{height:37px;background:var(--card);border-radius:6px;display:flex;align-items:center;padding:0 10px;font-size:8px;gap:8px}
.xcard .arr{margin-left:auto;width:14px;height:14px;border-radius:50%;border:1px solid var(--chipline);font-size:8px;display:flex;align-items:center;justify-content:center;color:var(--muted)}
.logo{border-radius:50%;flex:none;display:inline-block}
.xcard .logo{width:18px;height:18px}
.tabs{top:525px;left:55px;display:flex;gap:5px}
.tab{width:68px;height:20px;border-radius:3px;background:var(--soft);font-size:7px;display:flex;align-items:center;justify-content:center;color:var(--muted)}
.tab.on{background:var(--chip);color:var(--ink);border:1px solid var(--chipline)}
.dark .tab.on{background:#fff;color:#111}
.drop{top:525px;left:537px;width:69px;height:20px;background:var(--soft);border-radius:3px;font-size:7px;display:flex;align-items:center;justify-content:center;border:1px solid var(--chipline)}
/* table */
.table{top:563px;left:55px;width:551px}
.row{display:grid;grid-template-columns:20px 70px 66px 60px 66px 70px 68px 68px 63px;align-items:center;height:37px;border-bottom:1px solid var(--line);font-size:5.5px;font-weight:500}
.row>span:nth-child(n+4){text-align:right;padding-right:14px}
.row>span:nth-child(3){text-align:center}
.row.head{height:33px;font-size:5.5px;color:var(--muted);font-weight:500;line-height:9px}
.row.head span:nth-child(2){color:var(--ink);font-weight:600;padding-left:5px}
.row.sel{background:var(--hi);border-radius:3px}
.ex{display:flex;align-items:center;gap:4px;font-weight:600}
.ex .logo{width:10px;height:10px}
.ex i{font-style:normal;font-size:6px;color:var(--muted);margin-left:2px}
.star{text-align:center;color:#bbb;font-size:7px}
.star.on{color:#f5b300}
.g{color:var(--brand)}.r{color:var(--red)}
.pager{top:863px;left:482px;display:flex;gap:6px;font-size:6px;align-items:center}
.pager span{width:12px;height:12px;display:flex;align-items:center;justify-content:center;border-radius:2px}
.pager .box{background:var(--soft);border:1px solid var(--chipline)}
.pager .cur{border:1px solid var(--brand)}
/* charts */
.chartbox{background:var(--card);border-radius:6px}
.chartbox .drop{position:absolute;top:9px;left:13px;width:auto;padding:0 10px;background:var(--chip)}
.chartbox svg{position:absolute}
.kpis{top:1143px;left:55px;width:551px;display:grid;grid-template-columns:repeat(4,1fr);gap:14px}
.kpi{height:50px;border:1px solid var(--chipline);border-radius:4px;display:flex;align-items:center;padding:0 8px;gap:9px;background:var(--bg)}
.kpi .ic{width:22px;height:22px;border-radius:50%;background:var(--soft);border:1px solid var(--chipline)}
.kpi b{display:block;font-size:13px;font-weight:600}
.kpi small{font-size:6px}
/* compare */
.radar{top:1349px;left:55px;width:174px;height:247px;background:var(--card);border-radius:4px}
.dark .radar{background:#0f0f0f}
.scores{position:absolute;top:138px;left:0;right:0;font-size:5.5px}
.scores div{display:grid;grid-template-columns:60px 58px 40px;height:17px;align-items:center}
.scores div span:first-child{text-align:right;color:var(--muted);letter-spacing:.3px}
.scores div span:nth-child(2){padding-left:12px}
.cmp{top:1349px;left:244px;width:362px;height:378px;border:1px solid var(--line);border-radius:4px;background:var(--bg)}
.cmp .pick{position:absolute;top:9px;width:95px;height:19px;background:var(--soft);border:1px solid var(--chipline);border-radius:3px;font-size:6.5px;display:flex;align-items:center;justify-content:center}
.crow{display:grid;grid-template-columns:95px 94px 94px;column-gap:0;height:17px;align-items:center;font-size:5.5px;border-bottom:1px solid var(--line)}
.crow span:first-child{text-align:right;padding-right:5px;color:var(--muted)}
.crow span:nth-child(2){padding-left:56px}
.crow span:nth-child(3){padding-left:54px}
.crow.sec{height:33px;font-weight:700;color:var(--ink)}
.crow.sec span:first-child{color:var(--ink);font-weight:700;padding-right:0;text-align:right}
.crow.sec span:not(:first-child){color:var(--muted);font-weight:400}
/* faq */
.faq{top:1843px;left:55px;width:551px}
.q{height:29px;background:var(--card);border-radius:4px;display:flex;align-items:center;padding:0 11px;font-size:8.5px;margin-bottom:9.8px}
.q span{margin-left:auto;color:var(--brand3);font-size:11px}
/* footer */
.footer{top:2118px;left:0;right:0;height:170px;background:var(--foot);color:#fff}
.footer .brand{position:absolute;top:40px;left:55px}
.socials{position:absolute;top:94px;left:55px;display:flex;gap:7px}
.socials i{width:8px;height:8px;border-radius:50%;background:#fff;display:block}
.copy{position:absolute;top:118px;left:55px;font-size:6.5px}
.fcol{position:absolute;top:40px;font-size:6.5px;color:#9aa6a8;line-height:20px}
.fcol b{display:block;color:#fff;font-weight:500;font-size:8px;line-height:12px;margin-bottom:3px}
</style>
</head>
<body>

<!-- LIGHT THEME -->
<div class="page light">
  <header class="nav abs">
    <div class="brand"><span class="brand-dot"></span>Compare</div>
    <nav class="nav-links"><span>Features</span><span>Benefits</span><span>Services</span><span>Why Us</span><span>FAQs</span></nav>
    <div class="mode"><span>☀ Light</span><span class="on">☾ Dark</span></div>
    <span class="btn">Create Account</span>
  </header>
  <section class="hero abs">
    <div class="kicker">Discover the best <span class="accent">crypto Exchanges</span></div>
    <h1>Compare Crypto Exchages</h1>
    <p>Compare hundreds of cryptocurrency exchanges with ease. Discover key metrics, charts, and filters to find the best fit for you.</p>
    <span class="btn">Get Started</span>
  </section>
  <section class="band abs">
    <div class="stat" style="left:55px"><small>Platforms Tracked</small><b>+124 Platforms</b><small>As of Today</small></div>
    <div class="stat" style="left:174px"><small>Latest Update</small><b>Feb 16, 2025</b><small>Daily Update</small></div>
    <div class="stat" style="left:277px"><small>Happy Users</small><b>+15,000</b><small>As of Today</small></div>
    <span class="ghost" style="left:533px;top:21px;width:73px;height:20px">How We Test ›</span>
  </section>
  <div class="abs" style="top:393px;left:55px"><div class="eyebrow">Today's Top <span class="accent">Picks</span></div><div class="h2" style="margin-top:4px">Best Exchanges</div></div>
  <div class="abs" style="top:420px;right:56px;font-size:6.5px;font-weight:500">Affiliate Disclosure &nbsp;›</div>
  <div class="cards abs">
    <div class="xcard"><span class="logo" style="background:var(--blue)"></span>Coinvale<span class="arr">↗</span></div>
    <div class="xcard"><span class="logo" style="background:var(--gold)"></span>Binora<span class="arr">↗</span></div>
    <div class="xcard"><span class="logo" style="background:var(--violet)"></span>Krestel<span class="arr">↗</span></div>
    <div class="xcard"><span class="logo" style="background:var(--green)"></span>Bitmarsh<span class="arr">↗</span></div>
  </div>
  <div class="tabs abs"><span class="tab on">Fees</span><span class="tab">Features</span><span class="tab">Security</span></div>
  <div class="drop abs">Compare ⌄</div>
  <div class="table abs">
    <div class="row head"><span></span><span>Exchange</span><span>Last Updated</span><span>Maker Fee</span><span>Taker Fee</span><span>Features<br>Maker Fee</span><span>Features<br>Taker Fee</span><span>Trading Fee<br>Discount</span><span>Discount or<br>Bonus</span></div>
    <div class="row"><span class="star">☆</span><span class="ex"><span class="logo" style="background:var(--blue)"></span>Coinvale<i>↗</i></span><span>Feb 16, 2025</span><span>0.10%</span><span class="g">0.20%</span><span>$2.50</span><span>$5.00</span><span class="g">Yes</span><span class="g">10% Off</span></div>
    <div class="row sel"><span class="star on">★</span><span class="ex"><span class="logo" style="background:var(--gold)"></span>Binora<i>↗</i></span><span>Feb 16, 2025</span><span>0.15%</span><span class="r">0.45%</span><span>$3.00</span><span>$6.00</span><span class="r">No</span><span class="g">$1200 Bonus</span></div>
    <div class="row"><span class="star">☆</span><span class="ex"><span class="logo" style="background:var(--violet)"></span>Krestel<i>↗</i></span><span>Feb 16, 2025</span><span>0.12%</span><span class="g">0.25%</span><span>$3.00</span><span>$6.00</span><span class="g">Yes</span><span class="g">15% Discount</span></div>
    <div class="row"><span class="star">☆</span><span class="ex"><span class="logo" style="background:var(--green)"></span>Bitmarsh<i>↗</i></span><span>Feb 16, 2025</span><span>0.14%</span><span class="r">0.22%</span><span>$3.00</span><span>$6.00</span><span class="r">No</span><span>N/A</span></div>
    <div class="row"><span class="star">☆</span><span class="ex"><span class="logo" style="background:var(--orange)"></span>Bylark<i>↗</i></span><span>Feb 16, 2025</span><span>0.11%</span><span class="g">0.21%</span><span>$3.00</span><span>$6.00</span><span class="g">Yes</span><span class="g">20% Discount</span></div>
    <div class="row"><span class="star">☆</span><span class="ex"><span class="logo" style="background:#222"></span>Bullwick<i>↗</i></span><span>Feb 16, 2025</span><span>0.13%</span><span class="r">0.23%</span><span>$3.00</span><span>$6.00</span><span class="r">No</span><span class="g">20% Discount</span></div>
    <div class="row"><span class="star">☆</span><span class="ex"><span class="logo" style="background:#16b157"></span>Bitferro<i>↗</i></span><span>Feb 16, 2025</span><span>0.09%</span><span class="g">0.19%</span><span>$3.00</span><span>$6.00</span><span class="g">Yes</span><span class="g">25% Discount</span></div>
  </div>
  <div class="pager abs"><span class="box">‹</span><span class="cur">1</span><span>2</span><span>3</span><span>4</span><span>…</span><span class="box">›</span></div>
  <div class="chartbox abs" style="top:898px;left:55px;width:253px;height:209px">
    <span class="drop">Features Maker Fee ⌄</span>
    <svg style="top:44px;left:8px" width="235" height="150" viewBox="0 0 235 150" font-size="5.5" fill="currentColor">
      <g stroke="var(--line)" stroke-width=".8"><line x1="30" y1="8" x2="222" y2="8"/><line x1="30" y1="30" x2="222" y2="30"/><line x1="30" y1="53" x2="222" y2="53"/><line x1="30" y1="75" x2="222" y2="75"/><line x1="30" y1="98" x2="222" y2="98"/><line x1="30" y1="120" x2="222" y2="120"/><line x1="64" y1="8" x2="64" y2="120"/><line x1="97" y1="8" x2="97" y2="120"/><line x1="130" y1="8" x2="130" y2="120"/><line x1="163" y1="8" x2="163" y2="120"/><line x1="196" y1="8" x2="196" y2="120"/></g>
      <g text-anchor="end"><text x="25" y="10">$ 50</text><text x="25" y="32">$ 40</text><text x="25" y="55">$ 30</text><text x="25" y="77">$ 20</text><text x="25" y="100">$ 10</text><text x="25" y="122">0</text></g>
      <g fill="#3dbfa8"><rect x="35" y="57" width="19" height="63"/><rect x="68" y="48" width="19" height="72"/><rect x="101" y="34" width="19" height="86"/><rect x="134" y="32" width="19" height="88"/><rect x="167" y="41" width="19" height="79"/><rect x="200" y="79" width="19" height="41"/></g>
      <g text-anchor="middle"><text x="44" y="128">Coinvale</text><text x="77" y="128">Binora</text><text x="110" y="128">Krestel</text><text x="143" y="128">Bitmarsh</text><text x="176" y="128">Bylark</text><text x="209" y="128">Bullwick</text></g>
      <circle cx="44" cy="138" r="4" fill="var(--blue)"/><circle cx="77" cy="138" r="4" fill="var(--gold)"/><circle cx="110" cy="138" r="4" fill="var(--violet)"/><circle cx="143" cy="138" r="4" fill="var(--green)"/><circle cx="176" cy="138" r="4" fill="var(--orange)"/><circle cx="209" cy="138" r="4" fill="#222"/>
    </svg>
  </div>
  <div class="chartbox abs" style="top:898px;left:326px;width:280px;height:209px">
    <span class="drop">Trading Volume ⌄</span>
    <svg style="top:44px;left:8px" width="262" height="150" viewBox="0 0 262 150" font-size="5.5" fill="currentColor">
      <g stroke="var(--line)" stroke-width=".8"><line x1="24" y1="6" x2="250" y2="6"/><line x1="24" y1="31" x2="250" y2="31"/><line x1="24" y1="56" x2="250" y2="56"/><line x1="24" y1="81" x2="250" y2="81"/><line x1="24" y1="106" x2="250" y2="106"/><line x1="24" y1="131" x2="250" y2="131"/><line x1="64" y1="6" x2="64" y2="131"/><line x1="101" y1="6" x2="101" y2="131"/><line x1="138" y1="6" x2="138" y2="131"/><line x1="175" y1="6" x2="175" y2="131"/><line x1="212" y1="6" x2="212" y2="131"/></g>
      <g text-anchor="end"><text x="18" y="8">100</text><text x="18" y="33">80</text><text x="18" y="58">60</text><text x="18" y="83">40</text><text x="18" y="108">20</text><text x="18" y="133">0</text></g>
      <defs><linearGradient id="areaL" x1="0" y1="0" x2="0" y2="1"><stop offset="0" stop-color="#3dbfa8" stop-opacity=".55"/><stop offset="1" stop-color="#3dbfa8" stop-opacity=".08"/></linearGradient></defs>
      <path d="M46 61 L83 51 L120 36 L157 33 L194 43 L231 85 L231 131 L46 131Z" fill="url(#areaL)"/>
      <path d="M46 61 L83 51 L120 36 L157 33 L194 43 L231 85" fill="none" stroke="#2aa892" stroke-width="1"/>
      <g fill="#1f8f7c"><circle cx="46" cy="61" r="2"/><circle cx="83" cy="51" r="2"/><circle cx="120" cy="36" r="2"/><circle cx="157" cy="33" r="2"/><circle cx="194" cy="43" r="2"/><circle cx="231" cy="85" r="2"/></g>
      <g text-anchor="middle"><text x="46" y="141">Coinvale</text><text x="83" y="141">Binora</text><text x="120" y="141">Krestel</text><text x="157" y="141">Bitmarsh</text><text x="194" y="141">Bylark</text><text x="231" y="141">Bullwick</text></g>
    </svg>
  </div>
  <div class="kpis abs">
    <div class="kpi"><span class="ic"></span><div><b>125</b><small>Exchanges Tracked</small></div></div>
    <div class="kpi"><span class="ic"></span><div><b>0.15%</b><small>Average Trading Fee</small></div></div>
    <div class="kpi"><span class="ic"></span><div><b>892M</b><small>Total Users</small></div></div>
    <div class="kpi"><span class="ic"></span><div><b>12.2B</b><small>Web Visitors (30D)</small></div></div>
  </div>
  <div class="abs center" style="top:1280px"><div class="eyebrow">Best Crypto <span class="accent">Exchanges Tool</span></div><div class="h2">Compare Crypto Exchanges</div></div>
  <div class="radar abs">
    <svg width="174" height="130" viewBox="0 0 174 130" font-size="5" fill="var(--muted)">
      <g fill="none" stroke="var(--line)" stroke-width=".8"><polygon points="87,22 132,55 115,108 59,108 42,55"/><polygon points="87,40 115,60 104,93 70,93 59,60"/><polygon points="87,58 98,66 94,78 80,78 76,66"/></g>
      <polygon points="87,30 104,62 105,103 56,99 47,54" fill="#3b6fe8" fill-opacity=".65" stroke="#2f5fd6" stroke-width=".8"/>
      <polygon points="87,45 123,57 110,104 62,94 59,60" fill="#f0c75a" fill-opacity=".6" stroke="#d9a92c" stroke-width=".8"/>
      <text x="87" y="14" text-anchor="middle">Marker Fee</text><text x="134" y="45">Trading</text><text x="134" y="51">Fee</text><text x="5" y="53">Features Fee</text><text x="28" y="118">Takers Fee</text><text x="116" y="115">Discount</text><text x="116" y="121">or Bonus</text>
    </svg>
    <div class="scores">
      <div style="font-weight:600"><span></span><span style="color:var(--ink)">Coinvale</span><span>Binora</span></div>
      <div><span>FEES</span><span class="g">4.5/10</span><span class="r">3.4/10</span></div>
      <div><span>SECURITY</span><span class="g">7.8/10</span><span class="r">5.6/10</span></div>
      <div><span>FEATURES</span><span class="r">2.3/10</span><span class="g">9.1/10</span></div>
      <div><span>DEPOSITS</span><span class="g">6.7/10</span><span class="r">1.0/10</span></div>
      <div><span>WITHDRAWS</span><span class="r">1.2/10</span><span class="g">7.3/10</span></div>
    </div>
  </div>
  <div class="cmp abs">
    <span class="pick" style="left:68px">Coinvale ⌄</span>
    <span class="abs" style="top:13px;left:177px;width:11px;height:11px;border:1px solid var(--muted);border-radius:50%"></span>
    <span class="pick" style="left:199px">Binora ⌄</span>
    <div style="position:absolute;top:38px;left:0;right:0">
      <div class="crow sec"><span>FEATURES</span><span><i class="logo" style="width:11px;height:11px;background:var(--blue)"></i></span><span><i class="logo" style="width:11px;height:11px;background:var(--gold)"></i></span></div>
      <div class="crow"><span>Last Updated</span><span style="font-weight:600">Feb 16, 2025</span><span style="font-weight:600">Feb 16, 2025</span></div>
      <div class="crow"><span>Maker Fee</span><span class="r">0.10%</span><span class="g">0.15%</span></div>
      <div class="crow"><span>Taker Fee</span><span class="r">0.20%</span><span class="g">0.45%</span></div>
      <div class="crow"><span>Features Maker Fee</span><span class="r">$2.50</span><span class="g">$3.00</span></div>
      <div class="crow"><span>Features Taker Fee</span><span class="r">$5.00</span><span class="g">$6.00</span></div>
      <div class="crow"><span>Trading Fee Discount</span><span class="g">Yes</span><span class="r">No</span></div>
      <div class="crow"><span>Discount or Bonus</span><span class="g">70% Off</span><span class="r">$1200 Bonus</span></div>
      <div class="crow sec" style="height:50px;padding-top:18px"><span>SECURITY</span><span>-</span><span>-</span></div>
      <div class="crow sec"><span>FEES</span><span>-</span><span>-</span></div>
      <div class="crow sec"><span>DEPOSITS</span><span>-</span><span>-</span></div>
      <div class="crow sec"><span>WITHDRAWLS</span><span>-</span><span>-</span></div>
    </div>
    <span class="btn abs" style="top:342px;left:127px;width:108px;height:20px;font-size:6.5px">Full Comparison</span>
  </div>
  <div class="abs center" style="top:1781px"><div class="eyebrow">Popular <span class="accent">Exchanges Questions</span></div><div class="h2">Learn more about Crypto Exchage</div></div>
  <div class="faq abs">
    <div class="q">How does Crypto work?<span>+</span></div>
    <div class="q">Can I access Crypto from any country?<span>+</span></div>
    <div class="q">What types of digital currencies can I trade on Crypto?<span>+</span></div>
    <div class="q">What measures does Crypto take to protect user data?<span>+</span></div>
    <div class="q">What are the transaction costs associated with using Crypto?<span>+</span></div>
    <div class="q">What features does Crypto provide for experienced traders?<span>+</span></div>
  </div>
  <footer class="footer abs">
    <div class="brand"><span class="brand-dot"></span>Compare</div>
    <div class="socials"><i></i><i></i><i></i><i></i></div>
    <div class="copy">2025 Copyright. All rights reserved</div>
    <div class="fcol" style="left:268px"><b>About Us</b>About<br>Careers<br>Blog<br>Legal &amp; privacy</div>
    <div class="fcol" style="left:395px"><b>Services</b>Aplications<br>Buy Crypto<br>Affiliate<br>Institutional Services</div>
    <div class="fcol" style="left:527px"><b>Learn</b>What is Cryptocurrency?<br>Crypto Basic<br>Tips and Tutorials<br>Market Update</div>
  </footer>
</div>

<!-- DARK THEME -->
<div class="page dark">
  <header class="nav abs">
    <div class="brand"><span class="brand-dot"></span>Compare</div>
    <nav class="nav-links"><span>Features</span><span>Benefits</span><span>Services</span><span>Why Us</span><span>FAQs</span></nav>
    <div class="mode"><span>☀ Light</span><span class="on">☾ Dark</span></div>
    <span class="btn">Create Account</span>
  </header>
  <section class="hero abs">
    <div class="kicker">Discover the best <span class="accent">crypto Exchanges</span></div>
    <h1>Compare Crypto Exchages</h1>
    <p>Compare hundreds of cryptocurrency exchanges with ease. Discover key metrics, charts, and filters to find the best fit for you.</p>
    <span class="btn">Get Started</span>
  </section>
  <section class="band abs">
    <div class="stat" style="left:55px"><small>Platforms Tracked</small><b>+124 Platforms</b><small>As of Today</small></div>
    <div class="stat" style="left:174px"><small>Latest Update</small><b>Feb 16, 2025</b><small>Daily Update</small></div>
    <div class="stat" style="left:277px"><small>Happy Users</small><b>+15,000</b><small>As of Today</small></div>
    <span class="ghost" style="left:533px;top:21px;width:73px;height:20px">How We Test ›</span>
  </section>
  <div class="abs" style="top:393px;left:55px"><div class="eyebrow">Today's Top <span class="accent">Picks</span></div><div class="h2" style="margin-top:4px">Best Exchanges</div></div>
  <div class="abs" style="top:420px;right:56px;font-size:6.5px;font-weight:500">Affiliate Disclosure &nbsp;›</div>
  <div class="cards abs">
    <div class="xcard"><span class="logo" style="background:var(--blue)"></span>Coinvale<span class="arr">↗</span></div>
    <div class="xcard"><span class="logo" style="background:var(--gold)"></span>Binora<span class="arr">↗</span></div>
    <div class="xcard"><span class="logo" style="background:var(--violet)"></span>Krestel<span class="arr">↗</span></div>
    <div class="xcard"><span class="logo" style="background:var(--green)"></span>Bitmarsh<span class="arr">↗</span></div>
  </div>
  <div class="tabs abs"><span class="tab on">Fees</span><span class="tab">Features</span><span class="tab">Security</span></div>
  <div class="drop abs">Compare ⌄</div>
  <div class="table abs">
    <div class="row head"><span></span><span>Exchange</span><span>Last Updated</span><span>Maker Fee</span><span>Taker Fee</span><span>Features<br>Maker Fee</span><span>Features<br>Taker Fee</span><span>Trading Fee<br>Discount</span><span>Discount or<br>Bonus</span></div>
    <div class="row"><span class="star">☆</span><span class="ex"><span class="logo" style="background:var(--blue)"></span>Coinvale<i>↗</i></span><span>Feb 16, 2025</span><span>0.10%</span><span class="g">0.20%</span><span>$2.50</span><span>$5.00</span><span class="g">Yes</span><span class="g">10% Off</span></div>
    <div class="row sel"><span class="star on">★</span><span class="ex"><span class="logo" style="background:var(--gold)"></span>Binora<i>↗</i></span><span>Feb 16, 2025</span><span>0.15%</span><span class="r">0.45%</span><span>$3.00</span><span>$6.00</span><span class="r">No</span><span class="g">$1200 Bonus</span></div>
    <div class="row"><span class="star">☆</span><span class="ex"><span class="logo" style="background:var(--violet)"></span>Krestel<i>↗</i></span><span>Feb 16, 2025</span><span>0.12%</span><span class="g">0.25%</span><span>$3.00</span><span>$6.00</span><span class="g">Yes</span><span class="g">15% Discount</span></div>
    <div class="row"><span class="star">☆</span><span class="ex"><span class="logo" style="background:var(--green)"></span>Bitmarsh<i>↗</i></span><span>Feb 16, 2025</span><span>0.14%</span><span class="r">0.22%</span><span>$3.00</span><span>$6.00</span><span class="r">No</span><span>N/A</span></div>
    <div class="row"><span class="star">☆</span><span class="ex"><span class="logo" style="background:var(--orange)"></span>Bylark<i>↗</i></span><span>Feb 16, 2025</span><span>0.11%</span><span class="g">0.21%</span><span>$3.00</span><span>$6.00</span><span class="g">Yes</span><span class="g">20% Discount</span></div>
    <div class="row"><span class="star">☆</span><span class="ex"><span class="logo" style="background:#e8e8e8"></span>Bullwick<i>↗</i></span><span>Feb 16, 2025</span><span>0.13%</span><span class="r">0.23%</span><span>$3.00</span><span>$6.00</span><span class="r">No</span><span class="g">20% Discount</span></div>
    <div class="row"><span class="star">☆</span><span class="ex"><span class="logo" style="background:#16b157"></span>Bitferro<i>↗</i></span><span>Feb 16, 2025</span><span>0.09%</span><span class="g">0.19%</span><span>$3.00</span><span>$6.00</span><span class="g">Yes</span><span class="g">25% Discount</span></div>
  </div>
  <div class="pager abs"><span class="box">‹</span><span class="cur">1</span><span>2</span><span>3</span><span>4</span><span>…</span><span class="box">›</span></div>
  <div class="chartbox abs" style="top:898px;left:55px;width:253px;height:209px">
    <span class="drop">Features Maker Fee ⌄</span>
    <svg style="top:44px;left:8px" width="235" height="150" viewBox="0 0 235 150" font-size="5.5" fill="currentColor">
      <g stroke="var(--line)" stroke-width=".8"><line x1="30" y1="8" x2="222" y2="8"/><line x1="30" y1="30" x2="222" y2="30"/><line x1="30" y1="53" x2="222" y2="53"/><line x1="30" y1="75" x2="222" y2="75"/><line x1="30" y1="98" x2="222" y2="98"/><line x1="30" y1="120" x2="222" y2="120"/><line x1="64" y1="8" x2="64" y2="120"/><line x1="97" y1="8" x2="97" y2="120"/><line x1="130" y1="8" x2="130" y2="120"/><line x1="163" y1="8" x2="163" y2="120"/><line x1="196" y1="8" x2="196" y2="120"/></g>
      <g text-anchor="end"><text x="25" y="10">$ 50</text><text x="25" y="32">$ 40</text><text x="25" y="55">$ 30</text><text x="25" y="77">$ 20</text><text x="25" y="100">$ 10</text><text x="25" y="122">0</text></g>
      <g fill="#16937d"><rect x="35" y="57" width="19" height="63"/><rect x="68" y="48" width="19" height="72"/><rect x="101" y="34" width="19" height="86"/><rect x="134" y="32" width="19" height="88"/><rect x="167" y="41" width="19" height="79"/><rect x="200" y="79" width="19" height="41"/></g>
      <g text-anchor="middle"><text x="44" y="128">Coinvale</text><text x="77" y="128">Binora</text><text x="110" y="128">Krestel</text><text x="143" y="128">Bitmarsh</text><text x="176" y="128">Bylark</text><text x="209" y="128">Bullwick</text></g>
      <circle cx="44" cy="138" r="4" fill="var(--blue)"/><circle cx="77" cy="138" r="4" fill="var(--gold)"/><circle cx="110" cy="138" r="4" fill="var(--violet)"/><circle cx="143" cy="138" r="4" fill="var(--green)"/><circle cx="176" cy="138" r="4" fill="var(--orange)"/><circle cx="209" cy="138" r="4" fill="#e8e8e8"/>
    </svg>
  </div>
  <div class="chartbox abs" style="top:898px;left:326px;width:280px;height:209px">
    <span class="drop">Trading Volume ⌄</span>
    <svg style="top:44px;left:8px" width="262" height="150" viewBox="0 0 262 150" font-size="5.5" fill="currentColor">
      <g stroke="var(--line)" stroke-width=".8"><line x1="24" y1="6" x2="250" y2="6"/><line x1="24" y1="31" x2="250" y2="31"/><line x1="24" y1="56" x2="250" y2="56"/><line x1="24" y1="81" x2="250" y2="81"/><line x1="24" y1="106" x2="250" y2="106"/><line x1="24" y1="131" x2="250" y2="131"/><line x1="64" y1="6" x2="64" y2="131"/><line x1="101" y1="6" x2="101" y2="131"/><line x1="138" y1="6" x2="138" y2="131"/><line x1="175" y1="6" x2="175" y2="131"/><line x1="212" y1="6" x2="212" y2="131"/></g>
      <g text-anchor="end"><text x="18" y="8">100</text><text x="18" y="33">80</text><text x="18" y="58">60</text><text x="18" y="83">40</text><text x="18" y="108">20</text><text x="18" y="133">0</text></g>
      <defs><linearGradient id="areaD" x1="0" y1="0" x2="0" y2="1"><stop offset="0" stop-color="#1a8f7b" stop-opacity=".6"/><stop offset="1" stop-color="#1a8f7b" stop-opacity=".08"/></linearGradient></defs>
      <path d="M46 61 L83 51 L120 36 L157 33 L194 43 L231 85 L231 131 L46 131Z" fill="url(#areaD)"/>
      <path d="M46 61 L83 51 L120 36 L157 33 L194 43 L231 85" fill="none" stroke="#2aa892" stroke-width="1"/>
      <g fill="#67D7C9"><circle cx="46" cy="61" r="2"/><circle cx="83" cy="51" r="2"/><circle cx="120" cy="36" r="2"/><circle cx="157" cy="33" r="2"/><circle cx="194" cy="43" r="2"/><circle cx="231" cy="85" r="2"/></g>
      <g text-anchor="middle"><text x="46" y="141">Coinvale</text><text x="83" y="141">Binora</text><text x="120" y="141">Krestel</text><text x="157" y="141">Bitmarsh</text><text x="194" y="141">Bylark</text><text x="231" y="141">Bullwick</text></g>
    </svg>
  </div>
  <div class="kpis abs">
    <div class="kpi"><span class="ic"></span><div><b>125</b><small>Exchanges Tracked</small></div></div>
    <div class="kpi"><span class="ic"></span><div><b>0.15%</b><small>Average Trading Fee</small></div></div>
    <div class="kpi"><span class="ic"></span><div><b>892M</b><small>Total Users</small></div></div>
    <div class="kpi"><span class="ic"></span><div><b>12.2B</b><small>Web Visitors (30D)</small></div></div>
  </div>
  <div class="abs center" style="top:1280px"><div class="eyebrow">Best Crypto <span class="accent">Exchanges Tool</span></div><div class="h2">Compare Crypto Exchanges</div></div>
  <div class="radar abs">
    <svg width="174" height="130" viewBox="0 0 174 130" font-size="5" fill="var(--muted)">
      <g fill="none" stroke="#333" stroke-width=".8"><polygon points="87,22 132,55 115,108 59,108 42,55"/><polygon points="87,40 115,60 104,93 70,93 59,60"/><polygon points="87,58 98,66 94,78 80,78 76,66"/></g>
      <polygon points="87,30 104,62 105,103 56,99 47,54" fill="#1d47b8" fill-opacity=".75" stroke="#2f5fd6" stroke-width=".8"/>
      <polygon points="87,45 123,57 110,104 62,94 59,60" fill="#a8832c" fill-opacity=".65" stroke="#d9a92c" stroke-width=".8"/>
      <text x="87" y="14" text-anchor="middle">Marker Fee</text><text x="134" y="45">Trading</text><text x="134" y="51">Fee</text><text x="5" y="53">Features Fee</text><text x="28" y="118">Takers Fee</text><text x="116" y="115">Discount</text><text x="116" y="121">or Bonus</text>
    </svg>
    <div class="scores">
      <div style="font-weight:600"><span></span><span style="color:var(--ink)">Coinvale</span><span>Binora</span></div>
      <div><span>FEES</span><span class="g">4.5/10</span><span class="r">3.4/10</span></div>
      <div><span>SECURITY</span><span class="g">7.8/10</span><span class="r">5.6/10</span></div>
      <div><span>FEATURES</span><span class="r">2.3/10</span><span class="g">9.1/10</span></div>
      <div><span>DEPOSITS</span><span class="g">6.7/10</span><span class="r">1.0/10</span></div>
      <div><span>WITHDRAWS</span><span class="r">1.2/10</span><span class="g">7.3/10</span></div>
    </div>
  </div>
  <div class="cmp abs">
    <span class="pick" style="left:68px">Coinvale ⌄</span>
    <span class="abs" style="top:13px;left:177px;width:11px;height:11px;border:1px solid var(--muted);border-radius:50%"></span>
    <span class="pick" style="left:199px">Binora ⌄</span>
    <div style="position:absolute;top:38px;left:0;right:0">
      <div class="crow sec"><span>FEATURES</span><span><i class="logo" style="width:11px;height:11px;background:var(--blue)"></i></span><span><i class="logo" style="width:11px;height:11px;background:var(--gold)"></i></span></div>
      <div class="crow"><span>Last Updated</span><span style="font-weight:600">Feb 16, 2025</span><span style="font-weight:600">Feb 16, 2025</span></div>
      <div class="crow"><span>Maker Fee</span><span class="r">0.10%</span><span class="g">0.15%</span></div>
      <div class="crow"><span>Taker Fee</span><span class="r">0.20%</span><span class="g">0.45%</span></div>
      <div class="crow"><span>Features Maker Fee</span><span class="r">$2.50</span><span class="g">$3.00</span></div>
      <div class="crow"><span>Features Taker Fee</span><span class="r">$5.00</span><span class="g">$6.00</span></div>
      <div class="crow"><span>Trading Fee Discount</span><span class="g">Yes</span><span class="r">No</span></div>
      <div class="crow"><span>Discount or Bonus</span><span class="g">70% Off</span><span class="r">$1200 Bonus</span></div>
      <div class="crow sec" style="height:50px;padding-top:18px"><span>SECURITY</span><span>-</span><span>-</span></div>
      <div class="crow sec"><span>FEES</span><span>-</span><span>-</span></div>
      <div class="crow sec"><span>DEPOSITS</span><span>-</span><span>-</span></div>
      <div class="crow sec"><span>WITHDRAWLS</span><span>-</span><span>-</span></div>
    </div>
    <span class="btn abs" style="top:342px;left:127px;width:108px;height:20px;font-size:6.5px">Full Comparison</span>
  </div>
  <div class="abs center" style="top:1781px"><div class="eyebrow">Popular <span class="accent">Exchanges Questions</span></div><div class="h2">Learn more about Crypto Exchage</div></div>
  <div class="faq abs">
    <div class="q">How does Crypto work?<span>+</span></div>
    <div class="q">Can I access Crypto from any country?<span>+</span></div>
    <div class="q">What types of digital currencies can I trade on Crypto?<span>+</span></div>
    <div class="q">What measures does Crypto take to protect user data?<span>+</span></div>
    <div class="q">What are the transaction costs associated with using Crypto?<span>+</span></div>
    <div class="q">What features does Crypto provide for experienced traders?<span>+</span></div>
  </div>
  <footer class="footer abs">
    <div class="brand"><span class="brand-dot"></span>Compare</div>
    <div class="socials"><i></i><i></i><i></i><i></i></div>
    <div class="copy">2025 Copyright. All rights reserved</div>
    <div class="fcol" style="left:268px"><b>About Us</b>About<br>Careers<br>Blog<br>Legal &amp; privacy</div>
    <div class="fcol" style="left:395px"><b>Services</b>Aplications<br>Buy Crypto<br>Affiliate<br>Institutional Services</div>
    <div class="fcol" style="left:527px"><b>Learn</b>What is Cryptocurrency?<br>Crypto Basic<br>Tips and Tutorials<br>Market Update</div>
  </footer>
</div>

</body>
</html>
```